依頼詳細
集合場所が分かりにくいので、周辺が混みあうときには2~3本立てて、その目印に使います。なるべく目立つ印象で、明るく楽しい感じが伝わってくるものが良いです。写真も添付しますのでご利用ください。
記載項目
記載項目:鳥取砂丘でパラグライダー体験!
サイズ:一般的なのぼりのサイズ(600×1800ミリ)
希望イメージ
シンプル 複雑
単色 カラフル
暗い 明るい
日常 高級
遊び心 厳粛
未来的 伝統的
女性的 男性的
希望する色
青、黄、オレンジ
納品ファイル
• 高解像度JPG (.jpg)
• イラストレーター形式 (.ai)
補足説明
当方のHPは、
http://mina.kotoha.info/
になります。
画像等は、参考にしていただければと思います。
■ 選んだ理由

今回かなり悩みました。
期間をじっくり置いて、いろいろな視点ですべての作品を見させていただいた中で、写真を大きくはっきり使っていただいたのと、その配置が絶妙で、文字の自由度が大きくなる点を評価しました。
写真の切り取り方が良かったと思います。

■ 提案者全員のお礼・コメント

多数のご提案まことにありがとうございました。
甲乙つけがたいものが多くて、自分がどうこう評価するにはおこがましい感覚を受けながらも、みなさまの作品をじっくり拝見して、吟味させていただきました。
写真以外の可能性も感じたり、キャラや文字を面白くデフォルメしてくださったり、斬新な構図を見せてくださったり、う~んと感心ばかりしていました。
当方、まったくデザインに関して素人にも関わらず、いろいろなことを勉強させていただいたように思います。
皆さまの貴重な時間を、このたびは本当にありがとうございました。m(_ _)m

```html
<!DOCTYPE html>
<html lang="ja">
<head>
<meta charset="utf-8">
<title>鳥取砂丘でパラグライダー体験！</title>
<link rel="stylesheet" href="https://fonts.googleapis.com/css2?family=Noto+Sans+JP:wght@900&display=swap">
<style>
  :root {
    --page: #ffffff;
    --sky-deep: #1a3f9e;
    --sky: #3a6fc4;
    --wing-green: #8fb86a;
    --wing-purple: #a184b8;
    --wing-pink: #c98aa0;
    --sand: #cdbd9c;
    --sand-light: #e2d6bc;
    --title-blue: #1d2f8a;
    --hot-yellow: #ffe600;
    --hot-orange: #ff8a00;
    --hot-red: #e60012;
    --ink: #111111;
    --white: #ffffff;
  }
  * { margin: 0; padding: 0; box-sizing: border-box; }
  html, body {
    width: 846px; height: 1200px; overflow: hidden;
    background: var(--page);
  }
  .canvas { position: relative; width: 846px; height: 1200px; }
  .banner {
    position: absolute; left: 197px; top: 28px;
    width: 446px; height: 1114px; overflow: hidden;
  }
  .banner__photo {
    position: absolute; inset: 0;
    background: linear-gradient(180deg,
      var(--sky-deep) 0%, var(--sky) 22%,
      var(--wing-green) 40%, var(--wing-purple) 56%,
      var(--wing-pink) 68%, var(--sky) 82%,
      var(--sand-light) 90%, var(--sand) 100%);
  }
  .headline {
    position: absolute;
    writing-mode: vertical-rl;
    text-orientation: upright;
    font-family: "Noto Sans JP", sans-serif;
    font-weight: 900;
    line-height: 1;
    letter-spacing: 0;
    white-space: nowrap;
  }
  .headline__outline,
  .headline__fill { display: block; }
  .headline__outline { position: absolute; inset: 0; }
  .headline__fill { position: relative; }

  .place { left: 255px; top: 99px; font-size: 100px; }
  .place .headline__outline { color: var(--title-blue); -webkit-text-stroke: 18px var(--title-blue); }
  .place .headline__fill { color: var(--white); }

  .activity { left: 72px; top: 52px; font-size: 108px; }
  .activity .headline__outline { color: var(--white); -webkit-text-stroke: 14px var(--white); }
  .activity .headline__fill {
    color: var(--hot-yellow);
    -webkit-text-stroke: 3px var(--hot-red);
  }

  .experience { left: 230px; top: 690px; font-size: 132px; }
  .experience .headline__outline { color: var(--ink); -webkit-text-stroke: 20px var(--ink); }
  .experience .headline__fill { color: var(--white); }
</style>
</head>
<body>
<main class="canvas">
  <section class="banner">
    <div class="banner__photo" role="img" aria-label="青空に広がる色とりどりのパラグライダーの翼と、砂丘でグライダーを背負って歩く体験者たちの写真"></div>

    <h1 class="headline place">
      <span class="headline__outline" aria-hidden="true">鳥取砂丘で</span>
      <span class="headline__fill">鳥取砂丘で</span>
    </h1>
    <p class="headline activity">
      <span class="headline__outline" aria-hidden="true">パラグライダー</span>
      <span class="headline__fill">パラグライダー</span>
    </p>
    <p class="headline experience">
      <span class="headline__outline" aria-hidden="true">体験！</span>
      <span class="headline__fill">体験！</span>
    </p>
  </section>
</main>
</body>
</html>
```